Coffee pack for specialty coffee roasters

Tres Rios is a premium brand of specialty coffee roasters based in Prague in the Czech Republic.
We sell coffee beans to other coffee shops (wholesale channel) or to final consumers in our own coffee shops (retail)
We are roasting only specialty grade coffee that we source either directly or through specialty coffee merchants.
We have usually 6-8 coffees on our offer list. Each coffee stays with us 2-7 months based on their harvest season.
We pack our coffee for retail purposes in 250g bags that we sell in our cafés, roastery and clients.
We are now changing our bags from side gusset bags with valve closed by tin ties to flat bottom bags with zipper and valve.
We want evolution of our packaging design (not revolution)
Our current bags are decorated by front and back stickers.
New bags will be custom printed with general information and logo (e.g. Manufacturer information, contact, size etc.) and we want to have paper sleeve with customizable information (e.g. Name of the Coffee origin, farmer, taste profile, farm info etc.)

Target Market(s)

Men + woman aged 25-45, socioeconomical group A and B, university educated, interested in quality products, they care about what they drink and eat.

Industry/Entity Type

Coffee Shop

Font styles to use
Other font styles liked:
• Platform regular

Requirements
Must have
• Design of the pack itself and design of paper sleeve that will be excheangable (we need to change name of the coffee and information about it on the paper sleeve)
Nice to have
• nice to have- coffee related design on the bag under the sleeve
Should not have
• any crazy colours (the bag is golden with only black print on it) and sleeve can be colourful but nothing extravagant.

```html
<!DOCTYPE html>
<html lang="cs">
<head>
<meta charset="utf-8">
<title>Tres Rios – obal kávy 250 g, rozvinutý tvar</title>
<link href="https://fonts.googleapis.com/css2?family=Josefin+Sans:wght@300;400;600&family=Nunito+Sans:wght@400;600&family=Caveat:wght@500&display=swap" rel="stylesheet">
<style>
:root{
  --paper:#ffffff;
  --canvas:#ffffff;
  --ink:#111111;
  --black:#0b0907;
  --gold:#e2ad4f;
  --gold-soft:#d9a54a;
  --brown-1:#2a1a0c;
  --brown-2:#5a3a18;
  --fold:#9a9a9a;
  --cut:#e0322f;
  --bleed:#8fd3e6;
  --white:#ffffff;
}
*{margin:0;padding:0;box-sizing:border-box}
html,body{width:1200px;height:1000px;overflow:hidden;background:var(--canvas)}
body{position:relative;font-family:"Nunito Sans",sans-serif;color:var(--ink)}

.dim-top{position:absolute;left:40px;top:172px;width:1120px;height:20px;border-top:1px solid #777}
.dim-top::before,.dim-top::after{content:"";position:absolute;top:-6px;width:1px;height:12px;background:#777}
.dim-top::before{left:0}.dim-top::after{right:0}
.dim-top span{position:absolute;left:50%;top:-22px;transform:translateX(-50%);background:var(--canvas);padding:0 6px;font:400 20px "Josefin Sans",sans-serif}
.dim-side{position:absolute;left:1172px;top:205px;height:590px;border-left:1px solid #777}
.dim-side span{position:absolute;left:2px;top:50%;transform:translateY(-50%) rotate(90deg);font:400 14px "Josefin Sans",sans-serif;white-space:nowrap}
.dim-side-left{position:absolute;left:22px;top:490px;transform:rotate(-90deg);font-size:7px;color:#555}
.dim-bottom{position:absolute;left:40px;top:808px;width:1120px;height:14px;border-top:1px solid #777}
.dim-bottom .tick{position:absolute;top:-5px;width:1px;height:10px;background:#777}
.dim-bottom .lbl{position:absolute;top:2px;font-size:8px;color:#555;transform:translateX(-50%)}

.dieline{position:absolute;left:40px;top:205px;width:1120px;height:590px;background:var(--paper);outline:1px solid var(--bleed);outline-offset:4px}
.fold{position:absolute;top:0;height:342px;border-left:1px dashed var(--fold)}
.notch{position:absolute;width:0;height:0;border-top:5px solid transparent;border-bottom:5px solid transparent}
.notch.right{border-left:7px solid var(--cut)}
.notch.left{border-right:9px solid var(--cut)}
.tear{position:absolute;left:717px;width:403px;border-top:1.5px dashed var(--cut)}

.front-name{position:absolute;left:197px;width:363px;top:205px;text-align:center;font:400 58px/1 "Josefin Sans",sans-serif;letter-spacing:1px;color:var(--ink)}

.back-story{position:absolute;left:779px;top:146px;width:150px;font-size:8.6px;line-height:9.8px}
.back-name{position:absolute;left:960px;width:160px;top:200px;text-align:center;font:400 19px/1 "Josefin Sans",sans-serif;color:var(--ink)}
.back-legal{position:absolute;right:20px;top:228px;width:200px;text-align:right;font-size:7.4px;line-height:9px}
.back-legal p+p{margin-top:4px}
.back-weight{position:absolute;right:20px;top:290px;font-size:10px}
.back-weight b{font:600 25px "Josefin Sans",sans-serif;vertical-align:-3px}

.sleeve{position:absolute;left:0;top:342px;width:1120px;height:248px;background:var(--black);border-top:12px solid var(--gold);border-bottom:12px solid var(--gold);color:var(--white);overflow:hidden}
.sleeve-art{position:absolute;left:341px;top:0;width:779px;height:224px;background:linear-gradient(100deg,var(--brown-2) 0%,var(--brown-1) 45%,#4a3015 75%,#1a1108 100%)}
.sleeve-map{position:absolute;left:170px;top:0;width:171px;height:224px;background:radial-gradient(ellipse at 55% 55%,#3a2712 0%,#1c140b 60%,var(--black) 100%)}
.map-dot{position:absolute;left:244px;top:131px;width:12px;height:12px;border-radius:50%;background:var(--gold)}
.map-label{position:absolute;left:218px;top:192px;font:400 11px "Josefin Sans",sans-serif;color:var(--gold);letter-spacing:.5px}
.origin-story{position:absolute;left:37px;top:30px;width:131px;font-size:8.6px;line-height:11.6px;text-align:justify}
.origin-specs{position:absolute;left:230px;width:105px;top:35px;text-align:right;font:400 11.5px/13px "Josefin Sans",sans-serif}
.gold-rule{position:absolute;width:2px;background:var(--gold)}
.origin-name{position:absolute;left:348px;top:26px;font:400 44px/1 "Josefin Sans",sans-serif}
.farm-name{position:absolute;left:349px;top:70px;font:400 17px/1 "Josefin Sans",sans-serif}
.taste-notes{position:absolute;left:349px;top:111px;font:400 15px/15px "Josefin Sans",sans-serif}
.roast-date{position:absolute;left:350px;top:168px;width:187px;height:30px;background:var(--white);color:var(--ink);font:500 24px/30px "Caveat",cursive;padding-left:10px;letter-spacing:1px}
.dots{position:absolute;left:350px;top:197px;width:620px;height:6px;background:radial-gradient(circle,var(--gold) 1.8px,transparent 2.2px) 0 0/11px 6px repeat-x}

.flavor-wheel{position:absolute;left:586px;top:38px;width:140px;height:140px}
.flavor-wheel text{font:400 10.5px "Josefin Sans",sans-serif;fill:var(--white)}

.recipe-title{position:absolute;left:760px;width:96px;top:74px;text-align:right;font:400 12.5px/12px "Josefin Sans",sans-serif}
.recipe-row{position:absolute;left:865px;width:120px;display:flex;align-items:center;justify-content:flex-end;gap:8px}
.recipe-row .label{font:400 8.5px/10px "Josefin Sans",sans-serif;text-align:right}
.recipe-row .badge{width:38px;height:38px;border-radius:50%;background:var(--white);color:var(--ink);display:flex;align-items:center;justify-content:center;text-align:center;font-size:7.5px;line-height:8px;flex:none}
.taste-profile{position:absolute;left:994px;top:30px;width:120px;font-size:8.4px;line-height:11.6px}
.taste-profile h3{font:400 8.6px/11px "Josefin Sans",sans-serif;margin-bottom:6px}
.contacts{position:absolute;left:994px;top:186px;font-size:8.4px;line-height:11px}
</style>
</head>
<body>

<div class="dim-top"><span>370mm</span></div>
<div class="dim-side"><span>195mm</span></div>
<div class="dim-side-left">195</div>
<div class="dim-bottom">
  <div class="tick" style="left:0"></div><div class="tick" style="left:197px"></div><div class="tick" style="left:560px"></div><div class="tick" style="left:757px"></div><div class="tick" style="left:1119px"></div>
  <div class="lbl" style="left:98px">65</div><div class="lbl" style="left:378px">120</div><div class="lbl" style="left:658px">65</div><div class="lbl" style="left:938px">120</div>
</div>

<main class="dieline">
  <div class="fold" style="left:197px"></div>
  <div class="fold" style="left:560px"></div>
  <div class="fold" style="left:757px"></div>
  <div class="notch right" style="left:198px;top:45px"></div>
  <div class="notch left" style="left:549px;top:45px"></div>
  <div class="tear" style="top:74px"></div>
  <div class="tear" style="top:90px"></div>
  <div class="tear" style="top:106px"></div>

  <section class="front-panel">
    <div class="front-name">TRES RIOS</div>
  </section>

  <section class="back-panel">
    <p class="back-story">V ruce držíte čerstvě praženou zrnkovou kávu. Pracujeme výhradně s výběrovými jednodruhovými arabikami, které získaly 85+ bodů. Káva se sbírá na farmách ručně a my navazujeme, co nejpříměji, někdy i zcela osobní vazby na farmy. To vše, abychom vám mohli přinášet, to nejlepší, co se z aktuálních sklizní nabízet dá a podporovat přitom farmáře, kteří odvádí na svých farmách velmi tvrdou práci.</p>
    <div class="back-name">TRES RIOS</div>
    <div class="back-legal">
      <p>Výrobce: Tres Rios s.r.o.,<br>Korunní 2104/88, 130 00, Praha 3, ČR</p>
      <p>Minimální trvanlivost 90 dní od data<br>pražení uvedeného na zadní straně obalu</p>
      <p>Nejlepší chuti dosáhnete do 30 dnů od pražení kávy.</p>
    </div>
    <div class="back-weight">Hmotnost: <b>250</b>g</div>
  </section>

  <section class="sleeve">
    <div class="sleeve-map" role="img" aria-label="Mapa Jižní Ameriky s vyznačenou oblastí původu"></div>
    <div class="sleeve-art" role="img" aria-label="Ilustrace sběru a zpracování kávy v tlumených hnědých tónech"></div>

    <p class="origin-story">Jsme velmi hrdí, že tato káva se prezentuje v naší pražírně již počtvrté. V ruce držíte čerstvou sklizeň odrůdy caturra a pacas. Tato káva roste ve výšce kolem 1700 metrů nad mořem na svazích sopky Pichincha ve specifické biodiverzní oblasti mezi pralesem a Andami. Sklizeň této kávy probíhala mezi červencem a říjnem 2016 a byla sbírána výhradně ručně. Rok od roku také vidíme zlepšující se třídění a balení kávy. Kvalita je jednoduše hlavní prioritou farmáře Matea Varely.</p>

    <div class="map-dot"></div>
    <div class="map-label">PICHINCHA</div>
    <p class="origin-specs">100%<br>ARABICA CATURRA<br>ZPRACOVÁNÍ:<br>PROMYTÉ</p>
    <div class="gold-rule" style="left:340px;top:20px;height:204px"></div>

    <h1 class="origin-name">Ekvádor</h1>
    <h2 class="farm-name">FARMA: LOS ALISOS</h2>
    <p class="taste-notes">Lískové ořechy,<br>mléčná čokoláda,<br>karamel</p>
    <div class="roast-date">Praženo: 12.05.17</div>
    <div class="dots"></div>

    <svg class="flavor-wheel" viewBox="0 0 140 140" aria-label="Chuťový profil: aroma, kyselost, horkost, sladkost, dochuť, tělo">
      <g fill="none" transform="translate(70 76)">
        <polygon points="0,-46 40,-23 40,23 0,46 -40,23 -40,-23" stroke="#fff" stroke-width="3"/>
        <polygon points="0,-37 32,-18.5 32,18.5 0,37 -32,18.5 -32,-18.5" stroke="#e2ad4f" stroke-width="3"/>
        <polygon points="0,-28 24,-14 24,14 0,28 -24,14 -24,-14" stroke="#fff" stroke-width="2.5"/>
        <polygon points="0,-19 16.5,-9.5 16.5,9.5 0,19 -16.5,9.5 -16.5,-9.5" stroke="#e2ad4f" stroke-width="2.5"/>
        <polygon points="0,-10 8.7,-5 8.7,5 0,10 -8.7,5 -8.7,-5" stroke="#fff" stroke-width="2"/>
        <line x1="0" y1="-46" x2="0" y2="-52" stroke="#fff"/>
        <line x1="40" y1="-23" x2="45" y2="-26" stroke="#fff"/>
        <line x1="40" y1="23" x2="45" y2="26" stroke="#fff"/>
        <line x1="0" y1="46" x2="0" y2="52" stroke="#fff"/>
        <line x1="-40" y1="23" x2="-45" y2="26" stroke="#fff"/>
        <line x1="-40" y1="-23" x2="-45" y2="-26" stroke="#fff"/>
      </g>
      <text x="70" y="12" text-anchor="middle">Aroma</text>
      <text x="70" y="138" text-anchor="middle">Sladkost</text>
      <text x="73" y="80">6</text><text x="82" y="80">7</text><text x="91" y="80">8</text><text x="100" y="80">9</text><text x="110" y="80">10</text>
    </svg>
    <div style="position:absolute;left:605px;top:40px;font:400 10.5px 'Josefin Sans',sans-serif;width:140px">
      <span style="position:absolute;left:-7px;top:13px">Tělo</span>
      <span style="position:absolute;left:113px;top:13px">Kyselost</span>
      <span style="position:absolute;left:-13px;top:60px">Dochuť</span>
      <span style="position:absolute;left:113px;top:60px">Horkost</span>
    </div>

    <p class="recipe-title">DOPORUČENÝ<br>RECEPT NA<br>ESPRESSO</p>
    <div class="gold-rule" style="left:862px;top:18px;height:206px"></div>
    <div class="recipe-row" style="top:19px"><span class="label">GRAMÁŽ KÁVY<br>DO PORTAFILTERU</span><span class="badge">18g</span></div>
    <div class="recipe-row" style="top:68px"><span class="label">CÍLOVÁ<br>HMOTNOST<br>ESPRESSA</span><span class="badge">40g<br>45%</span></div>
    <div class="recipe-row" style="top:120px"><span class="label">CELKOVÝ ČAS<br>EXTRAKCE</span><span class="badge">28<br>sekund</span></div>

    <div class="taste-profile">
      <h3>CHUŤOVÝ<br>PROJEV ESPRESSA:</h3>
      <p>Ekvádor je na espressu krásně vybalancovaný s vůní pralinek a medu. V chuti se pak projevuje převážně chuť čokolády a másla s jemnou oříškovou dochutí. Díky tomu se hodí i na přípravu cappuccina a dalších mléčných variací.</p>
    </div>
    <p class="contacts">www.tres-rios.cz<br>@trroastery<br>FB/prazirnatresrios</p>
  </section>
</main>

</body>
</html>
```